Maravel - Refresh the look and feel of an existing website

We currently have an existing website www.maravelpartnersgroup.example however it needs a more refreshed 'look and feel'. We are a professional consultancy that works with large corporate organisations and government. Our 'tag line' is A New Way of Thinking. We want the site to communicate "Innovation" and Leading Edge Thinking.

Target Market(s)

Corporate and Professional Clients - Organisation and Business Change

Industry/Entity Type

Management Consulting

Number of Pages Required

1 page

Font styles to use
Sans Serif

Requirements
Must have
• Must have a professional Corporate look and feel. Header 'imagery' is ok but boxes on front page need changing ... along with the words. The focus on home page needs to 'call out' 3 main consulting areas:-
• - Change & Transformation Specialists
• - Innovative Solutions
• - Digital Transformation
• Tag Line for business is ... A New Way of Thinking (Highlighting Maravel as 'Thought Leaders' in business)
Nice to have
• Less "words' more imagery. Possibly an area for a 'video' or recent articles/blogs on the front page. Needs to have more of an 'interactive' feel. We are open to suggestions.
Should not have
• NA

```html
<!DOCTYPE html>
<html lang="en">
<head>
<meta charset="utf-8">
<title>Maravel Global Solutions</title>
<link href="https://fonts.googleapis.com/css2?family=Montserrat:wght@400;500;600;700;800&display=swap" rel="stylesheet">
<style>
  :root {
    --navy: #263e5a;
    --navy-deep: #1f344d;
    --charcoal: #343434;
    --chalk-light: #a7b4c1;
    --chalk-mid: #8493a3;
    --chalk-dark: #6d7c8c;
    --text: #2b3f57;
    --muted: #5a6b7d;
    --white: #ffffff;
    --rule: #c9d0d7;
  }
  * { margin: 0; padding: 0; box-sizing: border-box; }
  html, body { width: 1200px; height: 2226px; overflow: hidden; }
  body { position: relative; background: var(--white); font-family: 'Montserrat', sans-serif; color: var(--text); }
  .abs { position: absolute; }

  /* Hero */
  .hero-photo { left: 0; top: 0; width: 1200px; height: 676px;
    background: radial-gradient(ellipse at 70% 30%, var(--chalk-light) 0%, var(--chalk-mid) 55%, var(--chalk-dark) 100%); }
  .hero-person { left: 110px; top: 280px; width: 420px; height: 396px;
    background: linear-gradient(180deg, #b98a6a 0%, #d9c0ad 40%, #8d8d8d 70%, #3c3c3c 100%); opacity: .55;
    border-radius: 200px 200px 0 0; }
  .brand { left: 194px; top: 13px; height: 74px; display: flex; align-items: center; gap: 14px; }
  .brand-dot { width: 74px; height: 74px; border-radius: 50%; background: var(--navy); }
  .brand-name { color: var(--navy); font-weight: 600; line-height: 1; }
  .brand-name .main { display: block; font-size: 34px; letter-spacing: 1px; }
  .brand-name .sub { display: block; font-size: 14px; letter-spacing: 1.5px; margin-top: 2px; }
  .hero-social { left: 826px; top: 28px; display: flex; gap: 19px; }
  .hero-social span { width: 22px; height: 22px; border-radius: 50%; background: var(--navy); opacity: .8; }
  .tagline { left: 803px; top: 102px; color: var(--navy); font-weight: 700; font-size: 66px;
    line-height: 62px; letter-spacing: -3px; }

  /* Nav */
  .nav { left: 0; top: 676px; width: 1200px; height: 57px; background: var(--navy); }
  .nav a { position: absolute; top: 20px; color: var(--white); font-size: 11px; text-decoration: none; }
  .nav .sep { position: absolute; top: 18px; color: var(--white); font-size: 12px; }
  .nav .caret { position: absolute; left: 202px; top: 38px; width: 0; height: 0;
    border-left: 5px solid transparent; border-right: 5px solid transparent; border-top: 5px solid var(--white); }

  /* Intro */
  .intro-title { left: 0; top: 747px; width: 1260px; text-align: center; font-size: 17px; font-weight: 600; letter-spacing: .8px; color: var(--navy); }
  .intro-text { left: 378px; top: 779px; width: 444px; font-size: 7.2px; line-height: 10px; color: var(--muted); text-align: justify; }

  /* Service cards */
  .card-photo { top: 846px; width: 250px; height: 235px; }
  .card-photo.first { box-shadow: 0 6px 12px rgba(0,0,0,.35); }
  .card-panel { color: var(--white); }
  .card-panel svg { position: absolute; left: 0; top: 0; }
  .card-title { position: absolute; left: 23px; font-size: 10px; font-weight: 700; line-height: 12px; letter-spacing: .3px; }
  .card-text { position: absolute; left: 25px; width: 148px; font-size: 6.2px; line-height: 8.3px; text-align: justify; }
  .card-link { position: absolute; left: 0; width: 197px; text-align: center; font-size: 9.5px; font-weight: 700; }

  /* Recent events */
  .events-title { left: 194px; top: 1232px; font-size: 27px; font-weight: 700; letter-spacing: .8px; color: var(--navy); }
  .events-text { left: 194px; top: 1277px; width: 186px; font-size: 7.3px; line-height: 9.6px; text-align: justify; color: var(--navy); font-weight: 500; }
  .btn { left: 194px; top: 1431px; width: 94px; height: 27px; background: var(--navy); color: var(--white);
    font-size: 7.5px; font-weight: 600; display: flex; align-items: center; justify-content: center; }
  .video { left: 448px; top: 1177px; width: 526px; height: 341px;
    background: radial-gradient(ellipse at 65% 40%, #2f5a74 0%, #14293a 45%, #05090d 100%); }
  .play { left: 674px; top: 1309px; }

  /* Blogs */
  .blogs { left: 0; top: 1535px; width: 1200px; height: 425px; background: var(--navy); }
  .blogs-title { left: 0; top: 1552px; width: 1198px; text-align: center; color: var(--white); font-size: 16px; font-weight: 600; letter-spacing: .8px; }
  .avatar { left: 528px; top: 1607px; width: 142px; height: 142px; border-radius: 50%;
    background: radial-gradient(circle at 50% 45%, #b98a74 0%, #8a5e4b 45%, #4a2f27 100%); }
  .blog-text { left: 314px; top: 1776px; width: 570px; color: var(--white); font-size: 10px; line-height: 12.4px; text-align: justify; }
  .dots { left: 578px; top: 1945px; display: flex; gap: 3.5px; }
  .dots span { width: 8px; height: 8px; border-radius: 50%; background: #8d9bab; }
  .dots span.on { background: var(--white); }

  /* Footer */
  .foot-head { top: 1978px; font-size: 7.8px; font-weight: 500; color: var(--navy); }
  .foot-list { top: 2021px; list-style: none; font-size: 7.8px; color: var(--muted); }
  .foot-list li { height: 22px; }
  .foot-rule { top: 2013px; width: 1px; height: 104px; background: var(--rule); }
  .foot-social { top: 2024px; left: 914px; display: flex; flex-direction: column; gap: 8px; }
  .foot-social span { width: 23px; height: 23px; border-radius: 50%; border: 1px solid #d9dde2; }
  .foot-social .fill { background: #1e88c7; border-color: #1e88c7; }
  .copyright { left: 0; top: 2188px; width: 1200px; height: 38px; background: var(--navy); color: var(--white);
    font-size: 7.8px; font-weight: 600; display: flex; align-items: center; justify-content: center; }
</style>
</head>
<body>

<header>
  <div class="abs hero-photo" role="img" aria-label="Chalkboard backdrop with a woman looking up at a chalk-drawn thought bubble"></div>
  <div class="abs hero-person" role="img" aria-label="Woman in a striped top gazing upward"></div>
  <div class="abs brand">
    <span class="brand-dot"></span>
    <span class="brand-name"><span class="main">MARAVEL</span><span class="sub">GLOBAL SOLUTIONS</span></span>
  </div>
  <div class="abs hero-social" aria-label="Social links"><span></span><span></span><span></span><span></span></div>
  <h1 class="abs tagline">A New<br>Way of<br>Thinking</h1>
</header>

<nav class="abs nav">
  <a style="left:194px">Home</a><span class="caret"></span>
  <span class="sep" style="left:272px">|</span>
  <a style="left:321px">About Us</a>
  <span class="sep" style="left:411px">|</span>
  <a style="left:454px">Our Services</a>
  <span class="sep" style="left:561px">|</span>
  <a style="left:604px">Solutions</a>
  <span class="sep" style="left:693px">|</span>
  <a style="left:736px">What's Happening</a>
  <span class="sep" style="left:872px">|</span>
  <a style="left:916px">Contact Us</a>
</nav>

<section>
  <h2 class="abs intro-title">MARAVEL GLOBAL SOLUTIONS</h2>
  <p class="abs intro-text">Lorem Ipsum is simply dummy text of the printing and typesetting industry. Lorem Ipsum has been the industry's standard dummy text ever since the 1500s, when an unknown printer took a galley of type and scrambled it to make a type specimen book. It has survived not only five centuries, but also the leap into electronic type-</p>

  <div class="abs card-photo first" style="left:195px;background:linear-gradient(135deg,#f1f2f4 0%,#d5dae0 50%,#7d8791 100%)" role="img" aria-label="Presenter at a flipchart with an audience"></div>
  <div class="abs card-photo" style="left:459px;background:radial-gradient(circle at 55% 35%,#6fa8d8 0%,#2c5c8e 45%,#121e2c 100%)" role="img" aria-label="Hand touching a glowing network of people icons"></div>
  <div class="abs card-photo" style="left:723px;background:radial-gradient(circle at 50% 45%,#e8ecef 0%,#aab3bb 50%,#6c737a 100%)" role="img" aria-label="Team around a table with digital app icons"></div>

  <div class="abs card-panel" style="left:222px;top:963px;width:197px;height:196px">
    <svg width="197" height="196"><polygon points="0,57 197,0 197,196 0,196" fill="#263e5a"/></svg>
    <div class="card-title" style="top:78px">| Change &amp;<br>Transformation Specialists</div>
    <div class="card-text" style="top:108px">Lorem Ipsum is simply dummy text of the printing and typesetting industry. Lorem Ipsum has been the industry's standard dummy text ever since the 1500s, when an unknown printer took a galley of type and scrambled it to make a type speci-</div>
    <div class="card-link" style="top:175px">Read More</div>
  </div>
  <div class="abs card-panel" style="left:486px;top:963px;width:197px;height:152px">
    <svg width="197" height="152"><polygon points="0,60 197,0 197,152 0,152" fill="#343434"/></svg>
    <div class="card-title" style="top:85px">| Innovative Solutions</div>
    <div class="card-text" style="top:108px">Managers must effectively manage employees</div>
  </div>
  <div class="abs card-panel" style="left:750px;top:963px;width:197px;height:152px">
    <svg width="197" height="152"><polygon points="0,60 197,0 197,152 0,152" fill="#343434"/></svg>
    <div class="card-title" style="top:85px">| Digital Transformation</div>
    <div class="card-text" style="top:108px">Managers must effectively manage employees</div>
  </div>
</section>

<section>
  <h2 class="abs events-title">RECENT EVENTS</h2>
  <p class="abs events-text">Lorem Ipsum is simply dummy text of the printing and typesetting industry. Lorem Ipsum has been the industry's standard dummy text ever since the 1500s, when an unknown printer took a galley of type and scrambled it to make a type specimen book. It has survived not only five centuries, but also the leap into electronic typesetting, remaining essentially unchanged. It was popularised in the 1960s with the release of Letterform sheets containing Lorem Ipsum passages, and more recently with desktop publishing software like Pagewright Studio including versions of Lorem Ipsum.</p>
  <div class="abs btn">View all Video</div>
  <div class="abs video" role="img" aria-label="Hand on a tablet with floating media and message icons"></div>
  <svg class="abs play" width="72" height="72" viewBox="0 0 72 72">
    <circle cx="36" cy="36" r="33" fill="none" stroke="rgba(255,255,255,.55)" stroke-width="4"/>
    <polygon points="28,22 52,36 28,50" fill="rgba(255,255,255,.55)"/>
  </svg>
</section>

<section>
  <div class="abs blogs"></div>
  <h2 class="abs blogs-title">BLOGS</h2>
  <div class="abs avatar" role="img" aria-label="Portrait of the blog author"></div>
  <p class="abs blog-text">Lorem Ipsum is simply dummy text of the printing and typesetting industry. Lorem Ipsum has been the industry's standard dummy text ever since the 1500s, when an unknown printer took a galley of type and scrambled it to make a type specimen book. It has survived not only five centuries, but also the leap into electronic typesetting, remaining essentially unchanged. It was popularised in the 1960s with the release of Letterform sheets containing Lorem Ipsum passages, and more recently with desktop publishing software like Pagewright Studio including versions of Lorem Ipsum.<br>Lorem Ipsum is simply dummy text of the printing and typesetting industry. Lorem Ipsum has been the industry's standard dummy text ever since the 1500s, when an unknown printer took a galley of type and scrambled it to make a type specimen book. It has survived not only five centuries, but also the leap into electronic typesetting, remaining essentially unchanged. It was popularised in the 1960s with the release of Letterform sheets containing Lorem Ipsum passages, and more recently with desktop publishing software like Pagewright Studio including ver-</p>
  <div class="abs dots"><span class="on"></span><span></span><span></span><span></span></div>
</section>

<footer>
  <div class="abs foot-head" style="left:194px">About Us</div>
  <ul class="abs foot-list" style="left:194px"><li>Our Team</li><li>Our Values</li><li>Giving Back</li></ul>
  <div class="abs foot-rule" style="left:318px"></div>

  <div class="abs foot-head" style="left:398px">Our Services</div>
  <ul class="abs foot-list" style="left:398px"><li>Strategy and Design</li><li>Transformation</li><li>Change &amp; Culture</li><li>Organisational Development</li><li>Project Management</li><li>Organisational Efficiency</li><li>Specialist Placements</li></ul>
  <div class="abs foot-rule" style="left:562px"></div>

  <div class="abs foot-head" style="left:626px">Get In Touch</div>
  <ul class="abs foot-list" style="left:626px"><li>1300 555 019 (Aus)</li><li>0800 555 019 (NZ)</li><li>1300 555 020 (Intl)</li><li>info@maravelpartnersgroup.example</li></ul>
  <div class="abs foot-rule" style="left:823px"></div>

  <div class="abs foot-head" style="left:880px;width:94px;text-align:right">ALSO FOLLOW US ON</div>
  <div class="abs foot-social" aria-label="Social links"><span class="fill"></span><span></span><span></span><span></span></div>

  <div class="abs copyright">Copyright © 2014 Maravel Global Solutions</div>
</footer>

</body>
</html>
```